Business Card Design - Marla_BPH

We need a Business card for a new company based in Sydney Australia.
We distribute children's toys and educational products to Australian retailers.
Our clients are overseas manufacturers, Australian retail shop owners, schools, educational centres.
The design should communicate education and development for children.
The colours should be Australian primary bold colours. Green and Gold is an option to symbolise Australia.

Target Market(s)

Overseas manufacturers, Australian retail shop owners, Trade fairs

Industry/Entity Type

Education

Requirements
Must have
• BUSINESS CARD TO READ:

Marla Trescott
Managing Director

Tel: +61 452 918 306
Fax: +61 2 9364 2187
Marla@BrightPuddleHub.com.au

Bright Puddle Hub Pty Ltd
4/238 Wattlefield Rd.
Kestrel Cove, Sydney, NSW
Australia, 2079
www.BrightPuddleHub.com.au
Nice to have
• BACK OF THE BUSINESS CARD:

Images:

Fenna Ostrava
Rupert Tiny Snow Hare
Tiny Greta & Olof

same as business card example uploaded

```html
<!DOCTYPE html>
<html lang="en">
<head>
<meta charset="utf-8">
<title>Bright Puddle Hub – Business Card</title>
<link rel="stylesheet" href="https://fonts.googleapis.com/css2?family=Source+Sans+3:wght@400;700&family=Fredoka:wght@500&display=swap">
<style>
  :root {
    --card-white: #ffffff;
    --brand-blue: #3e58a8;
    --brand-red: #e0262c;
    --brand-green: #14a14a;
    --soft-lilac: #9b9fd0;
    --accent-lime: #c9d22b;
    --ink: #1a1a1a;
    --on-blue: #ffffff;
  }
  * { margin: 0; padding: 0; box-sizing: border-box; }
  html, body { width: 1200px; height: 686px; overflow: hidden; background: var(--card-white); }
  .card {
    position: relative;
    width: 1200px;
    height: 686px;
    font-family: "Source Sans 3", "Myriad Pro", sans-serif;
    background: var(--card-white);
  }
  .brand {
    position: absolute;
    left: 78px;
    top: 104px;
    display: flex;
    align-items: center;
    gap: 16px;
  }
  .brand-dot {
    width: 64px;
    height: 64px;
    border-radius: 50%;
    background: var(--brand-blue);
  }
  .brand-name {
    font-size: 52px;
    font-weight: 700;
    color: var(--brand-blue);
    line-height: 1;
    white-space: nowrap;
  }
  .brand-tagline {
    position: absolute;
    left: 283px;
    top: 232px;
    font-family: "Fredoka", "Arial Rounded MT Bold", sans-serif;
    font-weight: 500;
    font-size: 24px;
    color: var(--ink);
    letter-spacing: 0.3px;
  }
  .holder {
    position: absolute;
    left: 832px;
    top: 146px;
    font-size: 35px;
    line-height: 46px;
  }
  .holder .first { color: var(--brand-blue); }
  .holder .last { color: var(--brand-red); }
  .holder .role-a { color: var(--brand-green); }
  .holder .role-b { color: var(--soft-lilac); }
  .divider {
    position: absolute;
    left: 0; top: 315px;
    width: 1200px; height: 6px;
    background: var(--accent-lime);
  }
  .contact-band {
    position: absolute;
    left: 0; top: 321px;
    width: 1200px; height: 365px;
    background: var(--brand-blue);
    color: var(--on-blue);
    font-size: 24px;
    line-height: 33px;
  }
  .phones { position: absolute; left: 98px; top: 113px; }
  .phones .label { display: inline-block; width: 72px; }
  .email { position: absolute; left: 98px; top: 248px; }
  .address {
    position: absolute;
    right: 130px;
    top: 74px;
    text-align: right;
  }
  .web { position: absolute; right: 130px; top: 258px; }
</style>
</head>
<body>
  <div class="card">
    <div class="brand">
      <div class="brand-dot"></div>
      <div class="brand-name">Bright Puddle Hub</div>
    </div>
    <div class="brand-tagline">Australian Distributor</div>

    <div class="holder">
      <div><span class="first">Marla</span> <span class="last">Trescott</span></div>
      <div><span class="role-a">Managing</span> <span class="role-b">Director</span></div>
    </div>

    <div class="divider"></div>

    <div class="contact-band">
      <div class="phones">
        <div><span class="label">Tel&nbsp;:</span>+61 452 918 306</div>
        <div><span class="label">Fax&nbsp;:</span>+61 2 9364 2187</div>
      </div>
      <div class="email">Marla@BrightPuddleHub.com.au</div>
      <div class="address">
        <div>Bright Puddle Hub Pty Ltd</div>
        <div>4/238 Wattlefield Rd.</div>
        <div>Kestrel Cove, Sydney, NSW</div>
        <div>Australia, 2079</div>
      </div>
      <div class="web">www.BrightPuddleHub.com.au</div>
    </div>
  </div>
</body>
</html>
```